Eastfield Commercial Card

I would like a modern, eye catching card based off my logo design.
Info to include:
Anders Voll (Card Name)
eastfieldcommercial.example (Website)
555 203 8841 (Office/fax)
555 287 3096 (Business Cell)
anders@eastfieldcommercial.example (Work email)

Target Market(s)

Commercial real estate brokers, property owners.

Colors
ec1f27
757575

Requirements
Must have
• Name and info above. Not be lame!:)

```html
<!DOCTYPE html>
<html lang="en">
<head>
<meta charset="utf-8">
<title>Eastfield Commercial Card</title>
<link href="https://fonts.googleapis.com/css2?family=Montserrat:wght@600;700&family=Open+Sans:wght@400&display=swap" rel="stylesheet">
<style>
  :root {
    --brand-red: #a0181e;
    --brand-grey: #4a4a4a;
    --paper: #ecebe8;
    --backdrop: #cfc6bb;
    --ink: #2f2f2f;
  }
  * { box-sizing: border-box; margin: 0; padding: 0; }
  html, body { width: 1200px; height: 1200px; overflow: hidden; }
  body {
    background: var(--backdrop);
    display: flex;
    flex-direction: column;
    align-items: center;
    justify-content: center;
    gap: 44px;
    font-family: "Open Sans", sans-serif;
  }
  .card {
    width: 920px;
    height: 526px;
    background: var(--paper);
    box-shadow: 0 6px 18px rgba(0,0,0,0.15);
    position: relative;
  }
  .brand {
    display: flex;
    align-items: center;
    gap: 14px;
  }
  .brand-square {
    width: 30px;
    height: 30px;
    background: var(--brand-red);
  }
  .brand-name {
    font-family: "Montserrat", sans-serif;
    font-weight: 700;
    font-size: 34px;
    letter-spacing: 1px;
    text-transform: uppercase;
    color: var(--brand-red);
    white-space: nowrap;
  }
  .card-back {
    display: flex;
    align-items: center;
    justify-content: center;
  }
  .card-front .brand {
    position: absolute;
    left: 50px;
    top: 246px;
    gap: 10px;
  }
  .card-front .brand-name { font-size: 22px; letter-spacing: 0.5px; }
  .card-front .brand-square { width: 20px; height: 20px; }
  .growth-arrow {
    position: absolute;
    left: 456px;
    top: 108px;
    width: 44px;
    height: 310px;
  }
  .contact {
    position: absolute;
    left: 530px;
    top: 150px;
    width: 370px;
  }
  .contact-name {
    font-family: "Montserrat", sans-serif;
    font-weight: 700;
    font-size: 44px;
    color: var(--brand-red);
    text-transform: uppercase;
    letter-spacing: 0.5px;
    padding-bottom: 10px;
    border-bottom: 3px solid var(--brand-grey);
    margin-bottom: 16px;
    white-space: nowrap;
  }
  .contact-list { list-style: none; }
  .contact-item {
    display: flex;
    align-items: center;
    gap: 10px;
    font-size: 20px;
    line-height: 34px;
    color: var(--ink);
    white-space: nowrap;
  }
  .contact-item svg { width: 16px; height: 16px; flex: none; }
  .contact-item.small { font-size: 17px; }
</style>
</head>
<body>
  <section class="card card-back" aria-label="Card back">
    <div class="brand">
      <span class="brand-square"></span>
      <span class="brand-name">Eastfield Commercial</span>
    </div>
  </section>

  <section class="card card-front" aria-label="Card front">
    <div class="brand">
      <span class="brand-square"></span>
      <span class="brand-name">Eastfield Commercial</span>
    </div>

    <svg class="growth-arrow" viewBox="0 0 44 310" aria-hidden="true">
      <polygon points="22,0 44,52 26,40 26,310 18,310 18,40 0,52" fill="var(--brand-red)"/>
    </svg>

    <div class="contact">
      <div class="contact-name">Anders Voll</div>
      <ul class="contact-list">
        <li class="contact-item">
          <svg viewBox="0 0 16 16" aria-hidden="true"><path d="M3 1l3 3-1.6 2a9 9 0 0 0 5.6 5.6L12 10l3 3-2 2C6 15 1 10 1 3z" fill="var(--brand-red)"/></svg>
          555 203 8841
        </li>
        <li class="contact-item">
          <svg viewBox="0 0 16 16" aria-hidden="true"><rect x="4" y="1" width="8" height="14" rx="1.5" fill="var(--brand-red)"/><rect x="5.5" y="3" width="5" height="8" fill="var(--paper)"/></svg>
          555 287 3096
        </li>
        <li class="contact-item small">
          <svg viewBox="0 0 16 16" aria-hidden="true"><polygon points="1,8 15,1 11,15 8,9" fill="var(--brand-red)"/></svg>
          anders@eastfieldcommercial.example
        </li>
        <li class="contact-item small">
          <svg viewBox="0 0 16 16" aria-hidden="true"><path d="M6.5 9.5l3-3M7 4l1.5-1.5a2.8 2.8 0 0 1 4 4L11 8M9 12l-1.5 1.5a2.8 2.8 0 0 1-4-4L5 8" stroke="var(--brand-red)" stroke-width="1.8" fill="none" stroke-linecap="round"/></svg>
          eastfieldcommercial.example
        </li>
      </ul>
    </div>
  </section>
</body>
</html>
```